QM Fenwold Detailing, Inc.

I'm looking for business card design for an existing company with an existing logo/website. www.qmfenwold-detailing.com. VETERAN OWNED logo must be present.

Target Market(s)

Structural and architectural steel fabricators

Industry/Entity Type

Structural and architectural steel detailing and engineering

Contact Information for Business Card

logo, business name, address, phone, website, email, employee info

Font styles to use
Serif

Colors
00AB8E
00BBA5
67D7C9
C6EFE9
E9F9F6

Requirements
Must have
• company logo, website, VETERAN OWNED LOGO
Should not have
• Don't make it too busy. Less is more

```html
<!DOCTYPE html>
<html lang="en">
<head>
<meta charset="utf-8">
<title>QM Fenwold Detailing – Business Card</title>
<link rel="stylesheet" href="https://fonts.googleapis.com/css2?family=Cinzel:wght@700&family=Lora:wght@500;600&display=swap">
<style>
  :root{
    --stage:#9a9a9a;
    --navy:#02111f;
    --navy-2:#061c2c;
    --teal:#3fc4d2;
    --teal-deep:#0f5660;
    --white:#ffffff;
    --badge-red:#d8232c;
    --badge-blue:#1c4a8e;
  }
  *{box-sizing:border-box;margin:0;padding:0}
  html,body{width:966px;height:1200px;overflow:hidden;background:var(--stage)}
  .canvas{position:relative;width:966px;height:1200px}
  .card{position:absolute;left:67px;width:831px;height:475px;overflow:hidden;box-shadow:0 4px 10px rgba(0,0,0,.25)}
  .card--front{top:74px;background:radial-gradient(ellipse at 60% 45%,var(--navy-2),var(--navy) 70%)}
  .card--back{top:631px;background:var(--navy)}

  /* front */
  .brand{position:absolute;left:0;right:0;top:170px;display:flex;align-items:center;justify-content:center;gap:16px}
  .brand__mark{width:40px;height:40px;background:var(--teal)}
  .brand__name{font-family:"Lora",serif;font-weight:600;font-size:42px;color:var(--teal)}
  .web-band{position:absolute;left:50px;right:80px;top:363px;height:47px;
    background:linear-gradient(90deg,rgba(63,196,210,0) 0%,rgba(63,196,210,.35) 18%,#3fb3c2 55%,#48c3cf 80%,rgba(63,196,210,0) 100%);
    display:flex;align-items:center;justify-content:center;padding-right:20px}
  .web-band__url{font-family:"Lora",serif;font-weight:500;font-size:28px;color:var(--white)}

  /* back */
  .identity{position:absolute;left:0;top:0;width:338px;height:100%;background:var(--white)}
  .identity__brand{position:absolute;left:0;right:0;top:92px;display:flex;flex-direction:column;align-items:center;gap:12px}
  .identity__mark{width:40px;height:40px;background:var(--teal)}
  .identity__name{font-family:"Lora",serif;font-weight:600;font-size:26px;color:var(--teal);text-align:center;line-height:1.2}
  .vet-badge{position:absolute;left:94px;top:236px;width:150px;height:150px;border-radius:50%;
    background:linear-gradient(135deg,var(--badge-red) 0%,var(--badge-red) 42%,var(--badge-blue) 58%,var(--badge-blue) 100%)}
  .divider{position:absolute;left:338px;top:0;width:10px;height:100%;
    background:linear-gradient(180deg,var(--teal-deep),var(--teal) 50%,var(--teal-deep))}

  .person{position:absolute;left:396px;top:78px}
  .person__name{font-family:"Cinzel",serif;font-weight:700;font-size:36px;color:var(--white);letter-spacing:2px;line-height:1}
  .person__role{font-family:"Lora",serif;font-weight:600;font-size:18px;color:var(--white);margin-top:6px;letter-spacing:.5px}
  .person__rule{position:absolute;left:396px;top:149px;width:345px;height:2px;background:linear-gradient(90deg,var(--teal),rgba(63,196,210,0))}

  .contacts{position:absolute;left:399px;top:175px;list-style:none}
  .contact{display:flex;align-items:flex-start;gap:20px;font-family:"Lora",serif;font-weight:500;font-size:19px;color:var(--white);line-height:24px}
  .contact--phone{margin-bottom:24px}
  .contact--address{margin-bottom:22px}
  .contact--email{margin-bottom:22px}
  .contact__icon{flex:none;width:26px;height:26px;background:var(--teal);border-radius:2px;display:flex;align-items:center;justify-content:center}
  .contact__icon svg{width:18px;height:18px}
</style>
</head>
<body>
<div class="canvas">

  <section class="card card--front">
    <div class="brand">
      <span class="brand__mark"></span>
      <span class="brand__name">QM Fenwold Detailing</span>
    </div>
    <div class="web-band"><span class="web-band__url">www.qmfenwold-detailing.com</span></div>
  </section>

  <section class="card card--back">
    <div class="identity">
      <div class="identity__brand">
        <span class="identity__mark"></span>
        <span class="identity__name">QM Fenwold Detailing</span>
      </div>
      <div class="vet-badge" role="img" aria-label="U.S. veteran owned business badge" title="U.S. veteran owned business badge"></div>
    </div>
    <div class="divider"></div>

    <div class="person">
      <h1 class="person__name">DORIAN VALE</h1>
      <p class="person__role">CONSULTANT</p>
    </div>
    <div class="person__rule"></div>

    <ul class="contacts">
      <li class="contact contact--phone">
        <span class="contact__icon"><svg viewBox="0 0 24 24"><path fill="none" stroke="#02111f" stroke-width="2.2" stroke-linejoin="round" d="M5 3h4l2 5-2.5 1.5a11 11 0 0 0 6 6L16 13l5 2v4a2 2 0 0 1-2 2A16 16 0 0 1 3 5a2 2 0 0 1 2-2z"/></svg></span>
        <span>555.240.7183</span>
      </li>
      <li class="contact contact--address">
        <span class="contact__icon"><svg viewBox="0 0 24 24"><path fill="none" stroke="#02111f" stroke-width="2.2" d="M12 22s7-7.5 7-13a7 7 0 0 0-14 0c0 5.5 7 13 7 13z"/><circle cx="12" cy="9" r="2.5" fill="#02111f"/></svg></span>
        <span>4180 Harbor Crest Blvd.,<br>ste 310 Tampa, FL 33609</span>
      </li>
      <li class="contact contact--email">
        <span class="contact__icon"><svg viewBox="0 0 24 24"><rect x="3" y="6" width="18" height="12" fill="none" stroke="#02111f" stroke-width="2"/><path d="M3 6l9 7 9-7M3 18l7-6M21 18l-7-6" fill="none" stroke="#02111f" stroke-width="1.6"/></svg></span>
        <span>sales@qmfenwold-detailing.com</span>
      </li>
      <li class="contact contact--web">
        <span class="contact__icon"><svg viewBox="0 0 24 24"><g fill="none" stroke="#02111f" stroke-width="1.8"><circle cx="12" cy="12" r="9"/><ellipse cx="12" cy="12" rx="4" ry="9"/><path d="M3 12h18M5 7h14M5 17h14"/></g></svg></span>
        <span>www.qmfenwold-detailing.com</span>
      </li>
    </ul>
  </section>

</div>
</body>
</html>
```